Velvet Lantern rebranding my business with a new business card

I have my new logo and now I need a refresher on my business cards. I really want something fun and fresh. I like black background or anything to make the color pop.
Logo
Name: Velvet Lantern
Contact Info as stated below:
Mara Pelkin
519-555-0147
Logo
Name: Velvet Lantern
Mara Pelkin
519-555-0147
fb.me/VelvetLanternbyMara
Instagram: @VelvetLanternbyMara

Industry/Entity Type

Business

Contact Information for Business Card

double-sided. Logo on one side. Contact info on the other.

Requirements
Must have
• Logo
• Name: Velvet Lantern
• Contact Info as stated below:
• Mara Pelkin
• 519-555-0147
• fb.me/VelvetLanternbyMara
• fb.me/VelvetLanternbyMara

```html
<!DOCTYPE html>
<html lang="en">
<head>
<meta charset="utf-8">
<title>Velvet Lantern – Business Card</title>
<link rel="stylesheet" href="https://fonts.googleapis.com/css2?family=Open+Sans:wght@400;600&display=swap">
<style>
  :root {
    --backdrop: #3a302c;
    --card-white: #fbfbfb;
    --card-black: #1b1b1c;
    --name-pink: #e56f9c;
    --contact-red: #d4204f;
    --icon-pink: #e56f9c;
    --brand-pink: #f0a3c0;
  }
  html, body {
    margin: 0;
    padding: 0;
    width: 1200px;
    height: 844px;
    overflow: hidden;
    background: var(--backdrop);
    font-family: "Open Sans", Arial, sans-serif;
  }
  .canvas {
    position: relative;
    width: 1200px;
    height: 844px;
  }
  .card {
    position: absolute;
    top: 272px;
    width: 525px;
    height: 300px;
    border-radius: 3px;
    box-shadow: 0 10px 24px rgba(0,0,0,0.45);
    overflow: hidden;
  }
  .card--front { left: 50px; background: var(--card-white); }
  .card--back  { left: 625px; background: var(--card-black); }

  .contact-name {
    position: absolute;
    left: 40px;
    top: 140px;
    margin: 0;
    font-size: 22px;
    font-weight: 600;
    color: var(--name-pink);
  }
  .contact-list {
    position: absolute;
    left: 40px;
    top: 184px;
    margin: 0;
    padding: 0;
    list-style: none;
  }
  .contact-list li {
    display: flex;
    align-items: center;
    gap: 10px;
    height: 24px;
    font-size: 15px;
    color: var(--contact-red);
  }
  .contact-icon {
    width: 12px;
    height: 12px;
    flex: none;
    fill: var(--icon-pink);
  }

  .brand-mark {
    position: absolute;
    display: flex;
    flex-direction: column;
    align-items: center;
    gap: 14px;
  }
  .card--front .brand-mark { right: 22px; top: 28px; width: 210px; }
  .card--back .brand-mark { left: 50%; top: 50%; transform: translate(-50%, -50%); gap: 10px; }
  .brand-dot {
    border-radius: 50%;
    background: var(--brand-pink);
    flex: none;
  }
  .card--front .brand-dot { width: 180px; height: 180px; }
  .card--back .brand-dot { width: 110px; height: 110px; }
  .brand-name {
    font-weight: 600;
    white-space: nowrap;
    color: var(--name-pink);
  }
  .card--front .brand-name { font-size: 28px; }
  .card--back .brand-name { font-size: 20px; color: var(--brand-pink); }
</style>
</head>
<body>
<main class="canvas">

  <section class="card card--front" aria-label="Business card, contact side">
    <div class="brand-mark">
      <span class="brand-dot"></span>
      <span class="brand-name">Velvet Lantern</span>
    </div>

    <h1 class="contact-name">Mara Pelkin</h1>
    <ul class="contact-list">
      <li>
        <svg class="contact-icon" viewBox="0 0 12 12" aria-hidden="true">
          <path d="M2.5 0.8 L4.3 3 L3.4 4.3 Q4.5 6.8 7.7 8.6 L9 7.7 L11.2 9.5 L10 11.2 Q5.5 11 0.8 2 Z"/>
        </svg>
        519-555-0147
      </li>
      <li>
        <svg class="contact-icon" viewBox="0 0 12 12" aria-hidden="true">
          <rect x="0.5" y="2.5" width="11" height="7.5" rx="1"/>
          <path d="M1 3 L6 7 L11 3" stroke="#fff" stroke-width="1" fill="none"/>
        </svg>
        info@velvetlanternmail.com
      </li>
      <li>
        <svg class="contact-icon" viewBox="0 0 12 12" aria-hidden="true">
          <circle cx="6" cy="6" r="5.5"/>
          <path d="M0.8 6 H11.2 M6 0.8 Q3 6 6 11.2 M6 0.8 Q9 6 6 11.2" stroke="#fff" stroke-width="0.8" fill="none"/>
        </svg>
        www.velvetlanternshop.com
      </li>
      <li>
        <svg class="contact-icon" viewBox="0 0 12 12" aria-hidden="true">
          <circle cx="6" cy="6" r="4"/>
        </svg>
        fb.me/VelvetLanternbyMara
      </li>
    </ul>
  </section>

  <section class="card card--back" aria-label="Business card, logo side">
    <div class="brand-mark">
      <span class="brand-dot"></span>
      <span class="brand-name">Velvet Lantern</span>
    </div>
  </section>

</main>
</body>
</html>
```